International games company requires localisation design of gfa prediction game.

Using our current designs and those of our competitors, Brightwater Play are looking for novel design work that refreshes, enlivens and brings our games in line with what is expected in the American market. The Sports lottery game works by users selecting a winning margin for a series of 8 (in this case) GFA games. Should all of these predictions be correct, the user wins the jackpot.We are a software developer that creates free-to-play games specialised for the iGaming industry which function as customer acquisition and retention tools. Our user acquisition and retention models and processes are differentiated from our competitors by being driven by our unique style and application of gamification techniques and user behaviour analysis. Designs submitted should take inspiration from the attached images but designers should feel free to add their own flair and creativity whilst embracing intuitive UX and UI design principles.

Target Market(s)

American Sports fans aged 18+

Font styles to use
Sans Serif

Colors

Designer to choose colors to be used in the design.

Requirements
Must have
• User-friendly, intelligent design, applicable to being recoloured and branded to fit client's brands.

```html
<!DOCTYPE html>
<html lang="en">
<head>
<meta charset="utf-8">
<title>Brightwater Play – GFA Winning Margins</title>
<link rel="stylesheet" href="https://fonts.googleapis.com/css2?family=Open+Sans:wght@400;600;700;800&display=swap">
<style>
  :root {
    --black: #000000;
    --header-yellow: #f2c54c;
    --navy: #2d2e57;
    --gold: #f7d31e;
    --white: #ffffff;
    --green: #2eab5b;
    --red: #e8353a;
    --button-navy: #2c2d55;
    --card-white: #ffffff;
    --card-grey: #e8e8e8;
    --card-border: #c9c9c9;
    --text: #1c1c1c;
    --chip-gold-fill: #f3c95a;
    --chip-gold-line: #e6c467;
    --chip-tan-line: #b6a784;
    --chip-blue-line: #3b3f8e;
    --chip-orange-fill: #e5990f;
    --chip-orange-line: #d8a33a;
    --chip-teal-line: #31a8b8;
    --chip-red-line: #b52a2a;
    --chip-red-fill: #b8190f;
    --norsemen: #5a45c4;
    --pilgrims: #d5bd8a;
    --millers: #f0b41c;
    --tarpons: #2fc0c0;
    --hounds: #e2341d;
  }
  * { box-sizing: border-box; margin: 0; padding: 0; }
  html, body {
    width: 1200px; height: 2533px; overflow: hidden;
    background: var(--white);
    font-family: "Open Sans", sans-serif;
    color: var(--text);
  }
  .screen {
    position: relative;
    width: 540px; height: 1140px;
    transform: scale(2.2222);
    transform-origin: 0 0;
    overflow: hidden;
    background: var(--white);
  }
  .status-bar { position: absolute; left: 0; top: 0; width: 540px; height: 44px; background: var(--black); }
  .top-bar {
    position: absolute; left: 0; top: 44px; width: 540px; height: 83px;
    background: var(--header-yellow);
  }
  .back-button {
    position: absolute; left: 10px; top: 29px; width: 37px; height: 36px;
    border: 1.5px solid #222; border-radius: 3px;
    display: flex; align-items: center; justify-content: center;
  }
  .instruction {
    position: absolute; left: 84px; top: 16px;
    font-size: 20px; line-height: 24px; font-weight: 400; color: #111;
  }
  .autofill {
    position: absolute; left: 380px; top: 26px; width: 89px; height: 39px;
    background: var(--green); color: var(--white);
    font-size: 17px; font-weight: 600;
    display: flex; align-items: center; justify-content: center;
  }
  .close {
    position: absolute; left: 488px; top: 26px; width: 39px; height: 39px;
    background: var(--red);
    display: flex; align-items: center; justify-content: center;
  }
  .jackpot-band {
    position: absolute; left: 0; top: 127px; width: 540px; height: 209px;
    background: var(--navy); text-align: center;
  }
  .jackpot-win { position: absolute; left: 0; right: 0; top: 28px; font-size: 29px; font-weight: 700; color: var(--white); }
  .jackpot-amount { position: absolute; left: 0; right: 0; top: 61px; font-size: 47px; font-weight: 800; color: var(--gold); letter-spacing: 0.5px; }
  .jackpot-rule { position: absolute; left: 0; right: 0; top: 131px; font-size: 18px; font-weight: 400; color: var(--white); }
  .jackpot-consolation { position: absolute; left: 0; right: 0; top: 160px; font-size: 18px; font-weight: 400; color: var(--gold); }

  .fixture {
    position: absolute; left: 10px; width: 517px; height: 186px;
    border: 1px solid var(--card-border);
    box-shadow: 0 3px 5px rgba(0,0,0,0.25);
    background: var(--card-white);
  }
  .fixture.shaded { background: var(--card-grey); }
  .helmet { position: absolute; top: 15px; width: 57px; height: 58px; border-radius: 46% 50% 30% 40%; }
  .helmet.away { left: 38px; }
  .helmet.home { left: 225px; }
  .at { position: absolute; left: 144px; top: 30px; font-size: 30px; color: #111; }
  .team-name { position: absolute; top: 80px; width: 120px; text-align: center; font-size: 18px; color: #222; }
  .team-name.away { left: 7px; }
  .team-name.home { left: 193px; }
  .divider { position: absolute; left: 320px; top: 10px; width: 1px; height: 95px; background: #bdbdbd; }
  .action { position: absolute; left: 356px; width: 111px; height: 34px; color: var(--white); font-size: 17px; display: flex; align-items: center; justify-content: center; }
  .action.stats { top: 13px; background: var(--button-navy); }
  .action.bets { top: 63px; height: 35px; background: var(--red); }
  .rule { position: absolute; left: 8px; right: 5px; top: 113px; height: 1px; background: #bdbdbd; }
  .margins { position: absolute; left: 13px; top: 126px; display: flex; gap: 6px; }
  .chip {
    height: 32px; border: 1px solid var(--chip-tan-line); border-radius: 2px;
    background: var(--white); font-size: 16px; color: #222;
    display: flex; align-items: center; justify-content: center;
  }
  .w57 { width: 57px; } .w53 { width: 53px; } .w55 { width: 55px; } .w58 { width: 58px; } .w56 { width: 56px; } .w54 { width: 54px; }
  .chip.gold-fill { background: var(--chip-gold-fill); border-color: var(--chip-gold-fill); color: var(--white); }
  .chip.gold { border-color: var(--chip-gold-line); }
  .chip.blue { border-color: var(--chip-blue-line); }
  .chip.orange { border-color: var(--chip-orange-line); }
  .chip.orange-fill { background: var(--chip-orange-fill); border-color: var(--chip-orange-fill); color: var(--white); }
  .chip.teal { border-color: var(--chip-teal-line); }
  .chip.red { border-color: var(--chip-red-line); }
  .chip.red-fill { background: var(--chip-red-fill); border-color: var(--chip-red-fill); color: var(--white); }
</style>
</head>
<body>
<main class="screen">
  <div class="status-bar"></div>

  <header class="top-bar">
    <div class="back-button">
      <svg width="14" height="22" viewBox="0 0 14 22"><polyline points="11,2 3,11 11,20" fill="none" stroke="#222" stroke-width="1.8"/></svg>
    </div>
    <p class="instruction">Click the margins<br>to choose your winners</p>
    <div class="autofill">Autofill</div>
    <div class="close">
      <svg width="22" height="22" viewBox="0 0 22 22"><path d="M2 2 L20 20 M20 2 L2 20" stroke="#fff" stroke-width="2.6"/></svg>
    </div>
  </header>

  <section class="jackpot-band">
    <div class="jackpot-win">WIN</div>
    <div class="jackpot-amount">$ 1,000,000</div>
    <div class="jackpot-rule">PREDICT 8 WINNING MARGINS</div>
    <div class="jackpot-consolation">7 FROM 8 AND WIN $10,000</div>
  </section>

  <article class="fixture" style="top:352px">
    <div class="helmet away" role="img" aria-label="Norsemen team helmet" style="background:linear-gradient(160deg,#7462d8,var(--norsemen))"></div>
    <div class="at">@</div>
    <div class="helmet home" role="img" aria-label="Pilgrims team helmet" style="background:linear-gradient(160deg,#e2cfa4,var(--pilgrims))"></div>
    <div class="team-name away">Norsemen</div>
    <div class="team-name home">Pilgrims</div>
    <div class="divider"></div>
    <div class="action stats">Stats</div>
    <div class="action bets">Bets</div>
    <div class="rule"></div>
    <div class="margins">
      <div class="chip w57 gold-fill">+19</div>
      <div class="chip w53 gold">6-1</div>
      <div class="chip w55">1-6</div>
      <div class="chip w58">7-12</div>
      <div class="chip w55">13-18</div>
      <div class="chip w56">19-24</div>
      <div class="chip w55">24-29</div>
      <div class="chip w54">30+</div>
    </div>
  </article>

  <article class="fixture shaded" style="top:558px">
    <div class="helmet away" role="img" aria-label="Norsemen team helmet" style="background:linear-gradient(160deg,#7462d8,var(--norsemen))"></div>
    <div class="at">@</div>
    <div class="helmet home" role="img" aria-label="Millers team helmet" style="background:linear-gradient(160deg,#f6c94a,var(--millers))"></div>
    <div class="team-name away">Norsemen</div>
    <div class="team-name home">Millers</div>
    <div class="divider"></div>
    <div class="action stats">Stats</div>
    <div class="action bets">Bets</div>
    <div class="rule"></div>
    <div class="margins">
      <div class="chip w53 blue">+30</div>
      <div class="chip w53 blue">29-24</div>
      <div class="chip w58 blue">24-19</div>
      <div class="chip w56 blue">7-12</div>
      <div class="chip w57 orange-fill">13-18</div>
      <div class="chip w55 orange">19-24</div>
      <div class="chip w55 orange">24-29</div>
      <div class="chip w56 orange">30+</div>
    </div>
  </article>

  <article class="fixture" style="top:765px">
    <div class="helmet away" role="img" aria-label="Tarpons team helmet" style="background:linear-gradient(160deg,#55d3d3,var(--tarpons))"></div>
    <div class="at">@</div>
    <div class="helmet home" role="img" aria-label="Hounds team helmet" style="background:linear-gradient(160deg,#f0573f,var(--hounds))"></div>
    <div class="team-name away">Tarpons</div>
    <div class="team-name home">Hounds</div>
    <div class="divider"></div>
    <div class="action stats">Stats</div>
    <div class="action bets">Bets</div>
    <div class="rule"></div>
    <div class="margins">
      <div class="chip w57 teal">+19</div>
      <div class="chip w53 teal">6-1</div>
      <div class="chip w55 teal">1-6</div>
      <div class="chip w58 red">7-12</div>
      <div class="chip w55 red">13-18</div>
      <div class="chip w56 red-fill">19-24</div>
      <div class="chip w55 red">24-29</div>
      <div class="chip w54 red">30+</div>
    </div>
  </article>

  <article class="fixture shaded" style="top:970px">
    <div class="helmet away" role="img" aria-label="Norsemen team helmet" style="background:linear-gradient(160deg,#7462d8,var(--norsemen))"></div>
    <div class="at">@</div>
    <div class="helmet home" role="img" aria-label="Millers team helmet" style="background:linear-gradient(160deg,#f6c94a,var(--millers))"></div>
    <div class="team-name away">Norsemen</div>
    <div class="team-name home">Millers</div>
    <div class="divider"></div>
    <div class="action stats">Stats</div>
    <div class="action bets">Bets</div>
    <div class="rule"></div>
    <div class="margins">
      <div class="chip w53 blue">+30</div>
      <div class="chip w53 blue">29-24</div>
      <div class="chip w58 blue">24-19</div>
      <div class="chip w56 blue">7-12</div>
      <div class="chip w57 orange-fill">13-18</div>
      <div class="chip w55 orange">19-24</div>
      <div class="chip w55 orange">24-29</div>
      <div class="chip w56 orange">30+</div>
    </div>
  </article>
</main>
</body>
</html>
```